'WILD' eye catching Business Card Design / Logo for production company / TV host / adventurer

Hi there,

We are looking for a 'WILD' and exciting logo and double sided business card for our business "Red Kettle Studios".

Corwin Baxley is an international television host, adventurer, author and inspirational public speaker.

We want to project Corwin's talents onto his business card.

We are looking for a business card design that can carry over onto letter heads, emails etc. We want a design that is 'WILD', different and exciting.

Feel free to check out Corwin's web site: www.redkettlestudios.co.nz to get a better understanding what he is about.

Please feel free to go completely 'WILD' on this project as we want something different with lots of WOW factors.

Thank you so much and we look forward to your designs.

We have a feeling that there will be many more designs in the near future.

Best regards,

the production team

We have added another task to the list.

If the winning designer can also provide us with a matching letterhead and email signature based on the same style of design as the business card.

Target Market(s)

People with passion.

Industry/Entity Type

Business

Requirements
Must have
• Red Kettle Studios
Corwin Baxley
42 Fernhill Lane
Ashbury 7388
New Zealand

Phone +64-(0)3-5027 416
Cell +64-(0)274-861 052

email: redkettlenz@mailbox-example.nz
www.redkettlestuios.co.nz
Nice to have
• A feature made out of the name 'Red Kettle Studios'.

Corwin Baxley's name reasonably obvious.

All other details (except web site) can be quite small.

```html
<!DOCTYPE html>
<html lang="en">
<head>
<meta charset="utf-8">
<title>Red Kettle Studios – Business Card</title>
<link rel="stylesheet" href="https://fonts.googleapis.com/css2?family=Black+Ops+One&family=Cinzel:wght@600;700;800&display=swap">
<style>
  :root {
    --page: #e8e5df;
    --ink: #161616;
    --frame: #0c0c0c;
    --sky-top: #7fb4c4;
    --sky-mid: #cfe6dc;
    --haze: #e7efe0;
    --hills: #a9a873;
    --ground: #8a7a3e;
    --quote: #ffffff;
  }
  * { box-sizing: border-box; margin: 0; padding: 0; }
  html, body { width: 771px; height: 1200px; overflow: hidden; }
  body {
    position: relative;
    background: var(--page);
    font-family: "Cinzel", "Times New Roman", serif;
    color: var(--ink);
  }
  .card {
    position: absolute;
    border: 3px solid var(--frame);
    border-radius: 4px;
    overflow: hidden;
    box-shadow: 3px 4px 8px rgba(0,0,0,.45);
  }
  .scenery {
    position: absolute; inset: 0;
    background: linear-gradient(180deg,
      var(--sky-top) 0%, var(--sky-mid) 30%, var(--haze) 62%,
      var(--hills) 80%, var(--ground) 100%);
  }
  .card-front { left: 60px; top: 51px; width: 647px; height: 390px; }
  .card-back  { left: 190px; top: 491px; width: 393px; height: 649px; }

  .tagline {
    position: absolute; left: 22px; top: 52px;
    width: 150px; text-align: center;
    color: var(--quote); font-weight: 700; font-size: 13px; line-height: 15px;
    transform: rotate(-24deg);
    text-shadow: 0 1px 2px rgba(0,0,0,.35);
  }
  .brand-name {
    position: absolute; right: 30px; top: 32px; width: 280px;
    text-align: right;
    font-weight: 800; font-size: 34px; line-height: 40px;
    color: var(--ink);
  }
  .host-name {
    position: absolute; left: 170px; width: 420px; top: 170px;
    text-align: center;
    font-family: "Black Ops One", "Arial Black", sans-serif;
    font-size: 38px; letter-spacing: 2px;
    color: #2a2a2a;
    text-shadow: 2px 3px 3px rgba(0,0,0,.35);
  }
  .roles {
    position: absolute; left: 170px; width: 420px; top: 226px;
    text-align: center; font-weight: 600; font-size: 16.5px; line-height: 19px;
    font-variant: small-caps; color: var(--ink);
  }
  .front-web {
    position: absolute; left: 100px; width: 480px; top: 350px;
    text-align: center; font-weight: 800; font-size: 14px; letter-spacing: .5px;
  }

  .contact {
    position: absolute; left: 0; right: 0; top: 46px;
    text-align: center; font-weight: 700;
    text-shadow: 0 0 3px rgba(255,255,255,.8);
  }
  .contact-heading { font-size: 18px; line-height: 18px; }
  .contact-block { margin-top: 22px; font-size: 16px; line-height: 19px; }
  .contact-block.phones { margin-top: 20px; }
  .contact-block.online { margin-top: 20px; font-size: 13.5px; line-height: 19px; }
  .portrait {
    position: absolute; left: 78px; top: 299px; width: 233px; height: 309px;
    border: 3px solid var(--frame);
    background: linear-gradient(180deg, #d9d9d9 0%, #9a9a9a 35%, #3a3a3a 70%, #cfcfcf 100%);
    box-shadow: 2px 3px 6px rgba(0,0,0,.4);
  }
</style>
</head>
<body>
  <section class="card card-front">
    <div class="scenery" role="img" aria-label="Photo: a young man leaping from a grassy cliff edge into a cloudy sky above a wide green and golden valley"></div>
    <p class="tagline">“ …take that<br>first step.”</p>
    <h1 class="brand-name">Red Kettle Studios</h1>
    <h2 class="host-name">CORWIN BAXLEY</h2>
    <p class="roles">
      Television host - Adventurer - Author<br>
      Photographer - Inspirational speaker<br>
      Entrepreneur - World Traveller<br>
      Professional diver - guide
    </p>
    <p class="front-web">WWW.REDKETTLESTUDIOS.CO.NZ</p>
  </section>

  <section class="card card-back">
    <div class="scenery" role="img" aria-label="Photo: cloudy sky fading into a green and golden valley"></div>
    <div class="contact">
      <p class="contact-heading">Red Kettle Studios<br>Corwin Baxley</p>
      <p class="contact-block">42 Fernhill Lane<br>Ashbury 7388<br>New Zealand</p>
      <p class="contact-block phones">Phone: +64-(0)3-5027 416<br>Cell: +64-(0)274-861 052</p>
      <p class="contact-block online">redkettlenz@mailbox-example.nz<br>www.redkettlestudios.com</p>
    </div>
    <div class="portrait" role="img" aria-label="Black and white photo: the host in a sailing jacket steering a boat's wheel"></div>
  </section>
</body>
</html>
```